Pedal Wardens stationary
business card, letter head, powerpoint template
Creative Brief
Use same font as used in my logo
Tomas Lindqvo
Owner & Managing Director
Ekbackevägen 14 17452 Sundbyö
tomas@pedalwardens.cc
www.pedalwardens.cc
org.nr. 558213-4406
Business card and stationary design. We provide umpires & referees for teams/organizations.

```html
<!DOCTYPE html>
<html lang="en">
<head>
<meta charset="utf-8">
<title>Pedal Wardens – Business Card</title>
<link href="https://fonts.googleapis.com/css2?family=Josefin+Sans:wght@300&family=Open+Sans:wght@400;600&display=swap" rel="stylesheet">
<style>
  :root {
    --backdrop: #d9d9d9;
    --card-light: #fbfbfb;
    --card-mid: #e4e4e4;
    --card-edge: #bdbdbd;
    --ink: #2a2a2a;
    --ink-soft: #555555;
    --band-dark: #2b2b2b;
    --band-light: #4a4a4a;
    --band-text: #e8e8e8;
    --rule: #9a9a9a;
  }
  html, body {
    margin: 0;
    padding: 0;
    width: 1200px;
    height: 901px;
    overflow: hidden;
    background: var(--backdrop);
  }
  .canvas {
    position: relative;
    width: 1200px;
    height: 901px;
  }
  .card {
    position: absolute;
    left: 300px;
    width: 600px;
    height: 343px;
    border-radius: 22px;
    overflow: hidden;
    background: linear-gradient(160deg, var(--card-light) 0%, var(--card-mid) 70%, var(--card-edge) 100%);
    box-shadow: 0 10px 28px rgba(0,0,0,0.22);
  }
  .card--back { top: 68px; }
  .card--front { top: 490px; }

  .brand {
    position: absolute;
    display: flex;
    flex-direction: column;
    align-items: center;
  }
  .brand__dot {
    width: 44px;
    height: 44px;
    border-radius: 50%;
    background: var(--ink);
  }
  .brand__name {
    margin-top: 16px;
    font-family: "Josefin Sans", sans-serif;
    font-weight: 300;
    font-size: 27px;
    letter-spacing: 0.22em;
    color: var(--ink);
    text-transform: uppercase;
    white-space: nowrap;
  }
  .card--back .brand {
    left: 0; right: 0; top: 112px;
  }
  .card--back .web {
    position: absolute;
    left: 0; right: 0; top: 218px;
    text-align: center;
    font-family: "Open Sans", sans-serif;
    font-size: 14px;
    letter-spacing: 0.12em;
    color: var(--ink-soft);
  }

  .card--front .brand {
    left: 40px; width: 290px; top: 82px;
  }
  .contact {
    position: absolute;
    left: 362px;
    top: 86px;
    font-family: "Open Sans", sans-serif;
    color: var(--ink);
  }
  .contact__name {
    font-size: 17px;
    font-weight: 600;
    margin: 0;
  }
  .contact__role {
    font-size: 10.5px;
    color: var(--ink-soft);
    margin: 2px 0 18px;
  }
  .contact__address {
    font-size: 12px;
    line-height: 1.45;
    margin: 0 0 18px;
  }
  .contact__email {
    display: flex;
    align-items: center;
    gap: 10px;
    font-size: 12px;
  }
  .footer-rule {
    position: absolute;
    left: 0; right: 0;
    bottom: 60px;
    height: 2px;
    background: var(--rule);
  }
  .footer-band {
    position: absolute;
    left: 0; right: 0; bottom: 0;
    height: 52px;
    background: linear-gradient(180deg, var(--band-light), var(--band-dark));
    display: flex;
    align-items: center;
    justify-content: center;
    font-family: "Open Sans", sans-serif;
    font-size: 14px;
    letter-spacing: 0.3em;
    color: var(--band-text);
  }
</style>
</head>
<body>
<main class="canvas">
  <section class="card card--back" aria-label="Business card, back">
    <div class="brand">
      <div class="brand__dot"></div>
      <div class="brand__name">Pedal Wardens</div>
    </div>
    <div class="web">www.pedalwardens.cc</div>
  </section>

  <section class="card card--front" aria-label="Business card, front">
    <div class="brand">
      <div class="brand__dot"></div>
      <div class="brand__name">Pedal Wardens</div>
    </div>
    <div class="contact">
      <p class="contact__name">Tomas Lindqvo</p>
      <p class="contact__role">Owner &amp; Managing Director</p>
      <p class="contact__address">Ekbackevägen 14<br>17452 Sundbyö</p>
      <div class="contact__email">
        <svg width="14" height="10" viewBox="0 0 14 10" aria-hidden="true">
          <rect x="0.5" y="0.5" width="13" height="9" fill="none" stroke="#2a2a2a" stroke-width="1"/>
          <path d="M0.5 0.5 L7 5.5 L13.5 0.5" fill="none" stroke="#2a2a2a" stroke-width="1"/>
        </svg>
        <span>tomas@pedalwardens.cc</span>
      </div>
    </div>
    <div class="footer-rule"></div>
    <div class="footer-band">www.pedalwardens.cc</div>
  </section>
</main>
</body>
</html>
```